Hourgala promotional materials

Hourgala is a Canada-wide event that matches non-profits to skilled volunteers. The first part of the evening, attendees mix and mingle with the non-profits in the room. The second half of the evening is a a silent art auction where attendees bid their time, not their money, on artwork that we have purchased from local emerging artists. A successful bid maxes out at 100 volunteer hours. The Art-Winner has twelve months to complete their pledge before taking their artwork home as a sign of their good will.

We are not looking for someone to design a promotional postcards that sums up and reflects what we do.

We would like to play off of our current logo and colour palate- does not have to be directly lifted, it can be an interpretive riff. We want our branding to be instantly recognizable.

Here is a link to a video about what we do: http://www.hourgala-events.ca/

Target Market(s)

Young professionals who are community minded and interested in cultural products. We skew female and 25-40.

Industry/Entity Type

Artists

Font styles to use
Sans Serif

Requirements
Must have
• a) Hourgala colours: Green #7ac044, Grey #3e3e40
b) Hourgala logo should always use the 3 colour EPS version

Link to the Hourgala Logo:
https://hourgala.filedrop-host.com/hourgalalogo
Nice to have
• We want it to be modern, clean, fun, easy to read. The Hourgala can be complex to explain, so simplicity is key. We are open to "riffs" on our logo. For example, if you want to take one aspect or theme expressed by our logo and incorporate it into the design, we'd be interested to see what you could come up with. Nothing too trendy and faddish please as we'd like to use these designs across several seasons.
Should not have
• We don't want overly engineered or complex designs that we can't adapt.

```html
<!DOCTYPE html>
<html lang="en">
<head>
<meta charset="utf-8">
<title>Hourgala – Time Quote Postcard</title>
<link rel="stylesheet" href="https://fonts.googleapis.com/css2?family=Montserrat:wght@700&display=swap">
<style>
  :root {
    --periwinkle: #8482f7;
    --white: #ffffff;
    --brand-grey: #3e3e40;
    --ink: #111111;
  }
  html, body {
    margin: 0;
    padding: 0;
    overflow: hidden;
  }
  .postcard {
    position: relative;
    width: 847px;
    height: 1200px;
    background: var(--periwinkle);
    font-family: "Montserrat", sans-serif;
    font-weight: 700;
    color: var(--white);
    overflow: hidden;
  }
  .rule {
    position: absolute;
    left: 278px;
    width: 291px;
    height: 10px;
    background: var(--white);
  }
  .rule--top { top: 120px; }
  .rule--middle { top: 822px; }
  .rule--bottom { top: 923px; }
  .quote {
    position: absolute;
    top: 162px;
    left: 0;
    width: 100%;
    margin: 0;
    text-align: center;
    font-size: 55px;
    line-height: 89px;
    letter-spacing: 0.2px;
  }
  .quote span { display: block; }
  .attribution {
    position: absolute;
    top: 864px;
    left: 0;
    width: 100%;
    margin: 0;
    text-align: center;
    font-size: 22px;
    line-height: 30px;
  }
  .brand-tab {
    position: absolute;
    left: 278px;
    top: 992px;
    width: 291px;
    height: 208px;
  }
  .brand-tab svg {
    position: absolute;
    inset: 0;
    display: block;
  }
  .brand-name {
    position: absolute;
    top: 100px;
    left: 0;
    width: 100%;
    margin: 0;
    text-align: center;
    font-size: 30px;
    line-height: 36px;
    color: var(--brand-grey);
  }
  .brand-url {
    position: absolute;
    top: 154px;
    left: 0;
    width: 100%;
    margin: 0;
    text-align: center;
    font-size: 19px;
    line-height: 26px;
    color: var(--ink);
  }
</style>
</head>
<body>
  <main class="postcard">
    <div class="rule rule--top"></div>

    <blockquote class="quote">
      <span>My favourite</span>
      <span>things in life don’t</span>
      <span>cost money.</span>
      <span>It’s really clear that</span>
      <span>the most precious</span>
      <span>resource we all</span>
      <span>have is time.</span>
    </blockquote>

    <div class="rule rule--middle"></div>
    <p class="attribution">Sam Jordal</p>
    <div class="rule rule--bottom"></div>

    <footer class="brand-tab">
      <svg width="291" height="208" viewBox="0 0 291 208" aria-hidden="true">
        <polygon points="0,0 145.5,34 291,0 291,208 0,208" fill="var(--white)"/>
      </svg>
      <p class="brand-name">Hourgala</p>
      <p class="brand-url">www.hourgala-events.ca</p>
    </footer>
  </main>
</body>
</html>
```